Homestead Pipeworks Service (Let every tap run steady)

We are an innovative plumbing company with over 50years experience in all plumbing sectors. we cover all areas of Perth North and South and cover residential houses to warehouse and office plumbing systems.

we are fully licencesed and fully insured and all our Plumbers are police checked for your reassurance. we have plumbers who local to most areas so call out times are usally within the hour

our plumbers are located from Dawesville to Two Rocks our plumbers are very educated and all have a minimum off 10years experience on all Plumbing sytems and Hot water systems

we can cover your plumbing system for a year for one low price from $405+gst
this is the price of one visit from some plumbers

this includes unlimited call outs includes most materials and selected fittings

for this low price includes Leaks, Blockages , Hot water breakdowns, Burst pipes, and general plumbing repairs

have piece of mind that you can call us anytime any day and we will ease the stress of your plumbing emergency

Most common problem in the house is plumbing.and water can be the most destructive. Why not take the stress and worry of calling and hoping a plumber will turn up and the out of pocket expenses it will cost you.For a cost per year that can be paid weekly or monthly will cover you for unlimited call outs and most materials to cover most works undertaken.

This low price covers you for works undertaken and most materials and unlimited call outs

Prices start from $405 this is subject to a free plumbing inspection of your property

To make this even easier we allow weekly or monthly payments if set up with direct debit

OFFICE :08 9163 2058

Emergency 0436 815 372

EMAIL homesteadpipeworksservice@mailbrook.net

Target Market(s)

general public age range 25-80yrs old

Industry/Entity Type

Plumbing

Font styles to use
Sans Serif

Colors

Designer to choose colors to be used in the design.

Requirements
Must have
• emphasis on cost and set pays
• reliabie and trustworthy
• customer confidence
• value for money
Nice to have
• can be double sided

```html
<!DOCTYPE html>
<html lang="en">
<head>
<meta charset="utf-8">
<title>Homestead Pipeworks Service – Flyer</title>
<link rel="stylesheet" href="https://fonts.googleapis.com/css2?family=Open+Sans:ital,wght@0,400;0,600;0,700;0,800;1,400&family=Michroma&family=Crimson+Text:ital,wght@0,600;1,600&display=swap">
<style>
  :root{
    --navy:#1f3f8a;
    --red:#d9262b;
    --paper:#f3f4f6;
    --paper-edge:#e4e6ea;
    --ink:#56606e;
    --white:#ffffff;
    --stage:#e9e9ea;
  }
  *{box-sizing:border-box;margin:0;padding:0}
  html,body{width:1200px;height:1082px;overflow:hidden;background:var(--stage)}
  body{position:relative;font-family:"Open Sans",Arial,sans-serif}

  .flyer{position:absolute;left:240px;top:21px;width:720px;height:1040px;overflow:hidden;
    background:linear-gradient(180deg,var(--white),var(--paper) 60%,var(--paper-edge));
    box-shadow:0 6px 24px rgba(0,0,0,.18)}
  .shapes{position:absolute;inset:0}
  .abs{position:absolute}

  .brand{left:40px;top:48px;display:flex;align-items:center;gap:14px}
  .brand-dot{width:46px;height:46px;border-radius:50%;background:var(--red);flex:none}
  .brand-name{font-weight:800;font-size:27px;line-height:1.05;color:var(--navy);text-transform:uppercase;letter-spacing:.5px}
  .brand-tag{left:100px;top:120px;font-size:11px;font-weight:700;color:var(--navy);letter-spacing:.8px}

  .photo-plumber{left:392px;top:40px;width:360px;height:360px;border-radius:50%;
    background:radial-gradient(circle at 55% 45%,#c9ccd2,#7c8494 55%,#3a4354);
    border:10px solid var(--red);box-shadow:0 0 0 4px var(--white),0 0 0 8px var(--navy)}
  .photo-pipe{left:24px;top:868px;width:160px;height:160px;border-radius:50%;
    background:radial-gradient(circle at 50% 55%,#c98a52,#8a5a32 60%,#d9c2a0);
    border:8px solid var(--red);box-shadow:0 0 0 4px var(--white)}

  .headline{left:34px;top:206px;color:var(--navy)}
  .headline h1{font-family:"Michroma","Open Sans",sans-serif;font-size:36px;line-height:1.1;font-weight:400}
  .headline p{font-family:"Michroma","Open Sans",sans-serif;font-size:16px;line-height:1.35;margin-top:6px}

  .box{border-radius:22px;color:var(--white);font-size:13px;line-height:1.45}
  .box-intro{left:22px;top:372px;width:670px;padding:14px 22px;background:var(--red)}
  .box-intro p+p{margin-top:4px}

  .offer{left:42px;top:494px;width:320px;font-size:13px;line-height:1.45;color:var(--ink)}
  .offer p+p{margin-top:4px}

  .includes-pill{left:36px;top:606px;padding:6px 18px;border-radius:16px;background:var(--navy);
    color:var(--white);font-weight:700;font-size:16px}
  .includes-list{left:50px;top:642px;list-style:none;color:var(--navy);font-weight:800;font-size:16px;line-height:1.45}
  .includes-list li::before{content:"";display:inline-block;width:8px;height:8px;border-radius:50%;
    background:var(--navy);margin-right:8px;vertical-align:2px}

  .box-problem{left:382px;top:530px;width:312px;padding:16px 22px;background:var(--navy)}
  .box-mind{left:22px;top:776px;width:340px;padding:10px 20px;background:var(--red)}

  .badge{border-radius:50%;display:flex;flex-direction:column;align-items:center;justify-content:center;
    text-align:center;color:var(--white);font-family:"Crimson Text",Georgia,serif;font-weight:600;
    font-size:13px;line-height:1.15;box-shadow:0 0 0 6px var(--white),0 3px 10px rgba(0,0,0,.25);padding:16px}
  .badge strong{font-size:19px;font-style:italic}
  .badge-navy{left:380px;top:772px;width:134px;height:134px;background:var(--navy)}
  .badge-red{left:532px;top:800px;width:140px;height:140px;background:var(--red)}

  .payments{left:232px;top:950px;width:462px;text-align:right;font-family:"Crimson Text",Georgia,serif;
    font-style:italic;font-weight:600;font-size:14px;color:var(--navy)}
  .contacts{left:232px;top:972px;width:462px;text-align:right;color:var(--navy);font-size:15px;line-height:1.3}
</style>
</head>
<body>
<article class="flyer">
  <svg class="shapes" viewBox="0 0 720 1040" width="720" height="1040" aria-hidden="true">
    <path d="M0 158 C200 160 340 170 440 250 L440 266 C340 186 200 176 0 174Z" fill="#d9262b"/>
    <path d="M0 174 C200 176 340 186 440 266 L440 280 C340 200 200 190 0 188Z" fill="#1f3f8a"/>
    <path d="M0 1040 L0 980 C80 1000 200 1010 300 1040Z" fill="#1f3f8a"/>
    <path d="M300 1040 C380 1020 420 1000 440 990 L470 1040Z" fill="#d9262b"/>
  </svg>

  <div class="abs brand">
    <span class="brand-dot"></span>
    <div class="brand-name">Homestead<br>Pipeworks Service</div>
  </div>
  <div class="abs brand-tag">YOUR EMERGENCY PLUMBING COMPANY</div>

  <div class="abs photo-plumber" role="img" aria-label="Photo of a smiling plumber holding a pipe wrench and giving an OK sign"></div>

  <div class="abs headline">
    <h1>Plumbing<br>Service</h1>
    <p>Make Your Home<br>A Better Place For Living</p>
  </div>

  <div class="abs box box-intro">
    <p>We are fully licenced and fully insured and all our plumbers are police checked for your reassurance. We have plumbers who are local to most areas, so call out times are usually within the hour.</p>
    <p>Our plumbers are located from Dawesville to Two Rocks. Our plumbers are very educated and all have a minimum of 10 years experience on all plumbing systems and hot water systems.</p>
  </div>

  <div class="abs offer">
    <p>We can cover your plumbing system for a year for one low price from <strong>$405+gst</strong> – this is the price of one visit from some plumbers.</p>
    <p>This includes unlimited call outs, most materials and selected fittings.</p>
  </div>

  <div class="abs includes-pill">For this low price includes</div>
  <ul class="abs includes-list">
    <li>Leaks</li>
    <li>Blockages</li>
    <li>Hot water breakdowns</li>
    <li>Burst pipes</li>
    <li>General plumbing repairs</li>
  </ul>

  <div class="abs box box-problem">
    Most common problem in the house is plumbing, and water can be the most destructive. Why not take the stress and worry of calling and hoping a plumber will turn up, and the out of pocket expenses it will cost you. For a cost per year that can be paid weekly or monthly, you will be covered for unlimited call outs and most materials to cover most works undertaken.
  </div>

  <div class="abs box box-mind">
    Have peace of mind that you can call us anytime, any day and we will ease the stress of your plumbing emergency.
  </div>

  <div class="abs photo-pipe" role="img" aria-label="Close-up photo of a copper pipe joint"></div>

  <div class="abs badge badge-navy">
    <span>This</span><strong>low price</strong>
    <span>covers you for works undertaken and most materials and unlimited call outs</span>
  </div>
  <div class="abs badge badge-red">
    <span>Prices start from</span><strong>$405</strong>
    <span>this is subject to a free plumbing inspection of your property</span>
  </div>

  <p class="abs payments">To make this even easier we allow weekly or monthly payments if set up with direct debit</p>
  <div class="abs contacts">
    <div>homesteadpipeworksservice@mailbrook.net</div>
    <div>Office: 08 9163 2058</div>
    <div>Emergency: 0436 815 372</div>
  </div>
</article>
</body>
</html>
```